Logistics Website Design

See website https://tvarfreightglobal.com for theme and color details. Need the site to be re-done and reflect some of the designs shown in this list here: https://pinvora.com/tags/logistics-company-website

Target Market(s)

Logistics & Transportation

Industry/Entity Type

Logistics and Supply Chain

Coding

Coded - Design and coding required

Number of Pages Required

5+ page

Requirements
Must have
• Colors must match theme of logo. Looking for a sleek, interactive design.

```html
<!DOCTYPE html>
<html lang="en">
<head>
<meta charset="utf-8">
<title>Tvar Freight — Logistics</title>
<link rel="stylesheet" href="https://fonts.googleapis.com/css2?family=Archivo:wght@400;500;600;700&family=Barlow+Condensed:wght@600;700&family=Space+Grotesk:wght@400;500;700&display=swap">
<style>
:root{
  --bg:#1b0e0a;
  --bg-deep:#140a07;
  --panel:#2a1812;
  --orange:#ec6a3c;
  --cream:#f4e2d4;
  --muted:#b89a8b;
  --pink:#f2a890;
  --ink:#1a0f0b;
}
*{box-sizing:border-box;margin:0;padding:0}
html,body{width:1200px;height:3730px;overflow:hidden}
body{background:var(--bg);color:var(--cream);font-family:"Archivo",sans-serif;position:relative}
.display{font-family:"Barlow Condensed",sans-serif;font-weight:700;text-transform:uppercase;letter-spacing:0}
.cond{font-family:"Barlow Condensed",sans-serif;font-weight:600}
a{color:inherit;text-decoration:none}

/* nav */
.nav{position:absolute;top:0;left:0;width:1200px;height:115px;background:var(--bg-deep);display:flex;align-items:center;padding:0 30px}
.brand{display:flex;align-items:center;gap:10px;font-weight:700;font-size:17px;color:var(--orange)}
.brand i{width:22px;height:22px;border-radius:50%;background:var(--orange);display:block}
.menu{position:absolute;left:428px;top:46px;display:flex;gap:30px;font-family:"Barlow Condensed",sans-serif;font-size:16px;font-weight:600}
.menu a.active{color:var(--orange);border-bottom:2px solid var(--orange);padding-bottom:8px}
.btn-quote{position:absolute;right:34px;top:40px;width:110px;height:34px;background:var(--orange);color:var(--ink);border-radius:4px;font-family:"Barlow Condensed",sans-serif;font-size:15px;font-weight:700;display:flex;align-items:center;justify-content:center}

/* hero */
.hero{position:absolute;top:115px;left:0;width:1200px;height:710px;background:linear-gradient(180deg,#5b5048 0%,#6f5c48 38%,#3f2a1c 62%,#2a1a10 100%)}
.hero-shade{position:absolute;inset:0;background:linear-gradient(180deg,rgba(20,10,7,.1) 0%,rgba(20,10,7,.55) 55%,rgba(27,14,10,.95) 100%)}
.hero h1{position:absolute;top:412px;left:0;width:1200px;text-align:center;font-size:44px;line-height:50px;color:var(--cream);white-space:nowrap}
.hero p{position:absolute;top:484px;width:1200px;text-align:center;font-size:16px;color:#ecdcd0}
.hero .actions{position:absolute;top:533px;left:371px;display:flex;gap:22px}
.btn{height:58px;border-radius:6px;display:flex;align-items:center;justify-content:center;font-family:"Space Grotesk",sans-serif;font-weight:700;letter-spacing:2px;font-size:15px}
.btn-solid{width:210px;background:var(--orange);color:var(--ink)}
.btn-ghost{width:226px;border:2px solid var(--cream);color:var(--cream)}

/* stats */
.stats{position:absolute;top:825px;left:0;width:1200px;height:157px;background:#251409}
.stat{position:absolute;top:45px;border-left:2px solid var(--orange);padding-left:22px;height:66px}
.stat b{display:block;font-family:"Space Grotesk",sans-serif;font-size:44px;line-height:44px;font-weight:500}
.stat span{font-family:"Space Grotesk",sans-serif;font-size:13px;letter-spacing:1.5px;color:var(--muted);text-transform:uppercase}

/* solutions */
.solutions h2{position:absolute;top:1068px;left:30px;font-size:48px;line-height:56px}
.solutions .lede{position:absolute;top:1130px;left:30px;font-size:17px;color:#d8c3b5}
.tag-right{position:absolute;top:1112px;left:1040px;width:120px;border-top:2px solid #6a4a3c}
.tag-right span{position:absolute;top:16px;right:-10px;white-space:nowrap;color:var(--orange);font-family:"Barlow Condensed",sans-serif;font-size:16px;font-weight:700}
.card{position:absolute;width:555px;height:420px;border-radius:10px;overflow:hidden;background:linear-gradient(180deg,#4a2e23,#2e1a13)}
.card .photo{height:222px;display:block}
.card .body{position:absolute;top:222px;left:0;right:0;bottom:0;padding:0 30px}
.card svg.ico{position:absolute;left:30px;top:28px}
.card h3{position:absolute;top:28px;font-family:"Barlow Condensed",sans-serif;font-size:24px;font-weight:600;letter-spacing:.3px;white-space:nowrap}
.card p{position:absolute;top:78px;width:400px;font-size:12px;line-height:20px;color:#c9b3a5}
.card .more{position:absolute;top:148px;font-family:"Space Grotesk",sans-serif;font-size:13px;letter-spacing:1.2px;font-weight:700;color:var(--orange)}

/* tech */
.tech{position:absolute;top:2169px;left:0;width:1200px;height:747px;background:var(--pink);color:var(--ink)}
.pill{position:absolute;top:190px;left:30px;border:1px solid var(--ink);border-radius:14px;padding:5px 14px;font-family:"Space Grotesk",sans-serif;font-size:13px;letter-spacing:1.5px;font-weight:500}
.tech h2{position:absolute;top:230px;left:30px;width:520px;font-size:58px;line-height:56px}
.feat{position:absolute;left:30px;display:flex;gap:22px}
.feat .box{width:46px;height:46px;border-radius:6px;background:var(--ink);display:flex;align-items:center;justify-content:center;flex:none}
.feat h4{font-size:18px;font-weight:700;margin-top:2px}
.feat p{font-size:13px;line-height:16px;width:400px;margin-top:14px}
.tech-photo{position:absolute;left:628px;top:80px;width:552px;height:560px;border-radius:40px;transform:rotate(3deg);background:linear-gradient(160deg,#5b5a5c 0%,#3b3436 45%,#2a2022 70%,#5a3c2e 100%);box-shadow:0 30px 50px rgba(60,20,10,.35)}
.pulse{position:absolute;left:170px;top:170px;width:210px;height:210px;border:1px solid rgba(242,168,144,.5);border-radius:50%}
.pulse::before{content:"";position:absolute;inset:45px;border:1px solid rgba(242,168,144,.5);border-radius:50%}
.pulse-dot{position:absolute;left:242px;top:242px;width:66px;height:66px;border-radius:50%;background:var(--orange);display:flex;align-items:center;justify-content:center}

/* workflow */
.workflow h2{position:absolute;top:3006px;left:30px;font-size:48px;line-height:56px;white-space:nowrap}
.steps{position:absolute;top:3096px;left:30px;width:520px}
.step{position:absolute;left:0;padding-left:56px}
.step .num{position:absolute;left:0;top:0;width:36px;height:36px;border-radius:50%;border:2px solid var(--orange);font-family:"Space Grotesk",sans-serif;font-size:13px;display:flex;align-items:center;justify-content:center;background:var(--bg)}
.step.first .num{background:var(--orange);color:var(--ink)}
.step h4{font-family:"Barlow Condensed",sans-serif;font-size:20px;font-weight:600;margin-top:4px}
.step p{font-size:14px;line-height:22px;color:#c9b3a5;margin-top:10px;width:460px}
.rail{position:absolute;left:17px;top:36px;width:2px;height:234px;background:#5a3a2e}

.form{position:absolute;left:644px;top:3008px;width:526px;height:534px;background:var(--panel);border-radius:24px;padding:40px}
.form h3{font-family:"Barlow Condensed",sans-serif;font-size:30px;font-weight:600}
.field{position:absolute}
.field label{display:block;font-family:"Space Grotesk",sans-serif;font-size:11px;letter-spacing:1.4px;color:#c9b3a5;margin-bottom:10px}
.field .input{height:50px;border-radius:6px;background:#1e100b;padding:0 15px;display:flex;align-items:center;justify-content:space-between;font-size:14px;color:#7d6459}
.field .input.select{color:var(--cream)}
.form .submit{position:absolute;left:40px;top:396px;width:446px;height:58px;background:var(--orange);border-radius:8px;color:var(--ink);font-family:"Space Grotesk",sans-serif;font-weight:700;letter-spacing:3px;font-size:14px;display:flex;align-items:center;justify-content:center}
.form .trust{position:absolute;top:480px;left:0;width:526px;text-align:center;font-size:11px;color:#c9b3a5}

/* footer */
.footer{position:absolute;top:3632px;left:0;width:1200px;height:98px;background:var(--bg-deep);display:flex;align-items:center;padding:0 30px;font-family:"Space Grotesk",sans-serif;font-size:11px;color:var(--muted)}
.footer nav{margin-left:auto;display:flex;gap:44px}
</style>
</head>
<body>

<header class="nav">
  <a class="brand" href="https://tvarfreightglobal.com"><i></i>Tvar Freight</a>
  <nav class="menu">
    <a class="active" href="#">HOME</a><a href="#">SERVICES</a><a href="#">TRACKING</a><a href="#">ABOUT US</a>
  </nav>
  <a class="btn-quote" href="#">GET QUOTE</a>
</header>

<section class="hero" role="img" aria-label="Three white box trucks parked at a loading dock at dusk">
  <div class="hero-shade"></div>
  <h1 class="display">Bringing the world closer, one delivery at a time</h1>
  <p>High-precision logistics powered by next-gen telemetry. Moving the assets that move the world with industrial-grade reliability.</p>
  <div class="actions">
    <a class="btn btn-solid" href="#">START SHIPPING</a>
    <a class="btn btn-ghost" href="#">TRACK SHIPMENT</a>
  </div>
</section>

<section class="stats">
  <div class="stat" style="left:30px"><b>20K+</b><span>Monthly Users</span></div>
  <div class="stat" style="left:425px"><b>98%</b><span>Delivery Success</span></div>
  <div class="stat" style="left:820px"><b>GLOBAL</b><span>Network Coverage</span></div>
</section>

<section class="solutions">
  <h2 class="display">Core Logistics Solutions</h2>
  <p class="lede">Every route is optimized. Every container is monitored. Every delivery is a promise kept.</p>
  <div class="tag-right"><span>PRECISION DRIVEN</span></div>

  <article class="card" style="left:30px;top:1209px">
    <div class="photo" role="img" aria-label="Red semi truck with flatbed trailer under a pale sky" style="background:linear-gradient(180deg,#9fc0d2 0%,#b9cdd3 60%,#8a6a5a 100%)"></div>
    <div class="body">
      <svg class="ico" width="66" height="48" viewBox="0 0 66 48" fill="none" stroke="#f2a890" stroke-width="2"><rect x="4" y="18" width="34" height="16"/><path d="M38 22h12l8 8v4H38z"/><circle cx="14" cy="38" r="4"/><circle cx="50" cy="38" r="4"/></svg>
      <h3 style="left:124px">FLATBED TRANSPORTATION</h3>
      <p style="left:124px">From routine shipments to oversized and heavy-haul loads, we handle freight requiring proper securement, regulatory knowledge, and consistent on-time execution.</p>
      <a class="more" style="left:124px" href="#">LEARN MORE →</a>
    </div>
  </article>

  <article class="card" style="left:614px;top:1209px">
    <div class="photo" role="img" aria-label="White cab-over truck on a roadside with power lines and hills" style="background:linear-gradient(180deg,#5d7088 0%,#8b98a6 45%,#4f5a3f 100%)"></div>
    <div class="body">
      <svg class="ico" width="66" height="48" viewBox="0 0 66 48" fill="none" stroke="#f2a890" stroke-width="2"><path d="M4 12h30v22H4z"/><path d="M34 18h14l10 10v6H34z"/><circle cx="14" cy="38" r="4"/><circle cx="48" cy="38" r="4"/></svg>
      <h3 style="left:132px">STEP DECK TRANSPORTATION</h3>
      <p style="left:132px">Our step deck trucking services support tall, heavy, and specialized freight that requires additional height clearance and flexible loading options.</p>
      <a class="more" style="left:132px" href="#">LEARN MORE →</a>
    </div>
  </article>

  <article class="card" style="left:30px;top:1659px">
    <div class="photo" role="img" aria-label="White refrigerated truck in front of wooded hills" style="background:linear-gradient(180deg,#6c7478 0%,#4a4f45 45%,#9a9a98 100%)"></div>
    <div class="body">
      <svg class="ico" width="92" height="48" viewBox="0 0 92 48" fill="none" stroke="#f2a890" stroke-width="2"><rect x="4" y="10" width="58" height="24"/><path d="M62 16h14l10 10v8H62z"/><circle cx="16" cy="38" r="4"/><circle cx="74" cy="38" r="4"/></svg>
      <h3 style="left:151px">DRY VAN TRANSPORTATION</h3>
      <p style="left:151px">From consumer goods to industrial materials, our dry van services provide the space, security, and consistency you need coast to coast.</p>
      <a class="more" style="left:151px" href="#">LEARN MORE →</a>
    </div>
  </article>

  <article class="card" style="left:614px;top:1659px">
    <div class="photo" role="img" aria-label="Heavy haul truck with chrome stacks against green trees" style="background:linear-gradient(180deg,#3c4a2c 0%,#5a6a44 40%,#7e7e7c 100%);height:242px"></div>
    <div class="body" style="top:242px">
      <svg class="ico" width="92" height="48" viewBox="0 0 92 48" fill="none" stroke="#f2a890" stroke-width="2" style="top:26px"><path d="M4 14h58v18H4z"/><path d="M62 12h16l8 10v10H62z"/><circle cx="14" cy="36" r="4"/><circle cx="74" cy="36" r="4"/></svg>
      <h3 style="left:148px;top:26px">HEAVY HAUL TRANSPORTATION</h3>
      <p style="left:148px;top:74px">We provide heavy haul trucking solutions for oversized, overweight, and over-dimensional freight.</p>
      <a class="more" style="left:148px;top:128px" href="#">LEARN MORE →</a>
    </div>
  </article>
</section>

<section class="tech">
  <span class="pill">NEXT-GEN SYSTEMS</span>
  <h2 class="display">Powered by next-<br>gen technology</h2>
  <div class="feat" style="top:392px">
    <div class="box"><svg width="20" height="20" viewBox="0 0 20 20" fill="none" stroke="#f2a890" stroke-width="1.6"><path d="M3 16V11M8 16V8M13 16V10M18 16V5M3 8l5-4 5 3 5-4"/></svg></div>
    <div><h4>Real-Time Telemetry</h4><p>Live data streaming from every vehicle in our fleet, ensuring route efficiency and asset safety.</p></div>
  </div>
  <div class="feat" style="top:491px">
    <div class="box"><svg width="20" height="20" viewBox="0 0 20 20" fill="none" stroke="#f2a890" stroke-width="1.6"><circle cx="10" cy="10" r="2.5"/><circle cx="3" cy="4" r="1.6"/><circle cx="17" cy="4" r="1.6"/><circle cx="3" cy="16" r="1.6"/><circle cx="17" cy="16" r="1.6"/><path d="M4.5 5.5 8 8M15.5 5.5 12 8M4.5 14.5 8 12M15.5 14.5 12 12"/></svg></div>
    <div><h4>Automated Hubs</h4><p>Smart sorting centers that reduce transit downtime by up to 40% using AI-driven routing.</p></div>
  </div>
  <div class="tech-photo" role="img" aria-label="Semi truck with trailer on a highway at sunset">
    <div class="pulse"></div>
    <div class="pulse-dot"><svg width="24" height="24" viewBox="0 0 24 24" fill="none" stroke="#1a0f0b" stroke-width="1.8"><rect x="4" y="4" width="16" height="16" rx="2"/><path d="M8 16v-4M12 16V8M16 16v-6"/></svg></div>
  </div>
</section>

<section class="workflow">
  <h2 class="display">Streamlined Workflow</h2>
  <div class="steps">
    <div class="rail"></div>
    <div class="step first" style="top:0"><span class="num">1</span><h4>REQUEST A QUOTE</h4><p>Tell us what you’re moving and where. Our AI engine generates the most efficient route and price point instantly.</p></div>
    <div class="step" style="top:126px"><span class="num">2</span><h4>SMART ONBOARDING</h4><p>Assets are tagged with biometric sensors and synced to your dashboard for real-time tracking.</p></div>
    <div class="step" style="top:252px"><span class="num">3</span><h4>GLOBAL DISPATCH</h4><p>Your cargo enters our kinetic ecosystem, monitored 24/7 until the final proof of delivery.</p></div>
  </div>

  <form class="form">
    <h3>START YOUR SHIPMENT</h3>
    <div class="field" style="left:40px;top:108px;width:212px"><label>ORIGIN</label><div class="input">e.g. New York, USA</div></div>
    <div class="field" style="left:274px;top:108px;width:212px"><label>DESTINATION</label><div class="input">e.g. Hamburg, DE</div></div>
    <div class="field" style="left:40px;top:206px;width:446px"><label>SERVICE TYPE</label><div class="input select">Select Logistics Type<svg width="12" height="8" viewBox="0 0 12 8" fill="none" stroke="#c9b3a5" stroke-width="1.5"><path d="M1 1l5 5 5-5"/></svg></div></div>
    <div class="field" style="left:40px;top:306px;width:446px"><label>WORK EMAIL</label><div class="input">corporate@company.com</div></div>
    <div class="submit">CALCULATE ESTIMATE</div>
    <p class="trust">Trusted by 450+ Top 500 Enterprises worldwide.</p>
  </form>
</section>

<footer class="footer">
  <span>© 2026. An independent agent of Hale Marrow LLC.</span>
  <nav><a href="#">Privacy Policy</a><a href="#">Terms of Service</a><a href="#">Cookie Policy</a><a href="#">Contact Support</a></nav>
</footer>

</body>
</html>
```